A label for my commercially sold local honey. This is a LABEL not a logo

3 inches high
2 inches wide

Target Market(s)

Customers who like "local" honey

Logo Text

Wildflower Honey -- 100% Pure & Unfiltered -- Florida

Logo styles of interest
Wordmark Logo
Requirements
Must have
• Wildflower Honey -- 100% Pure & Unfiltered -- Florida

Florida should be dominant

3 inches high / 2 inches wide

```html
<!DOCTYPE html>
<html lang="en">
<head>
<meta charset="utf-8">
<title>Wildflower Honey Label</title>
<link href="https://fonts.googleapis.com/css2?family=Barlow:wght@400;600;700&family=Bebas+Neue&family=Pacifico&display=swap" rel="stylesheet">
<style>
  :root {
    --paper: #ffffff;
    --ink: #1c1c1c;
    --ornament: #e6e6e6;
    --honey-top: #f3a21f;
    --honey-mid: #f7b326;
    --honey-low: #f4801f;
    --honey-base: #ee5b22;
    --honey-shadow: #d9641a;
    --cream: #fff4c8;
    --bee-yellow: #f6c431;
    --bee-dark: #2a2a2a;
  }
  html, body {
    margin: 0;
    padding: 0;
    width: 800px;
    height: 1200px;
    overflow: hidden;
    background: var(--paper);
  }
  .label {
    position: relative;
    width: 800px;
    height: 1200px;
    overflow: hidden;
    background: var(--paper);
    font-family: "Barlow", Arial, sans-serif;
  }
  .ornament {
    position: absolute;
    border-radius: 0 0 0 60%;
    background: radial-gradient(circle at 70% 20%, var(--ornament), rgba(230,230,230,0) 72%);
  }
  .ornament--left {
    left: 0; top: 0; width: 170px; height: 90px;
    border-radius: 0 0 60% 0;
    background: radial-gradient(circle at 20% 10%, var(--ornament), rgba(230,230,230,0) 75%);
  }
  .ornament--right { right: 0; top: 0; width: 260px; height: 230px; }
  .brand {
    position: absolute;
    top: 190px;
    left: 0;
    width: 800px;
    text-align: center;
    font-weight: 600;
    font-size: 40px;
    letter-spacing: 2px;
    color: var(--ink);
  }
  .honey {
    position: absolute;
    left: 0; top: 290px;
    width: 800px; height: 910px;
  }
  .bee {
    position: absolute;
    border-radius: 50%;
    background: radial-gradient(circle, var(--bee-yellow) 0 40%, var(--bee-dark) 41% 55%, rgba(255,255,255,0.35) 56% 100%);
    opacity: 0.9;
  }
  .bee--upper { left: 620px; top: 410px; width: 84px; height: 74px; }
  .bee--lower { left: 30px; top: 640px; width: 84px; height: 74px; }
  .title-script {
    position: absolute;
    top: 440px; left: 0; width: 800px;
    text-align: center;
    font-family: "Pacifico", cursive;
    font-size: 80px;
    line-height: 1;
    color: #fff;
    transform: rotate(-3deg);
    text-shadow: 4px 5px 0 var(--honey-shadow);
  }
  .title-main {
    position: absolute;
    top: 552px; left: 0; width: 800px;
    text-align: center;
    font-family: "Bebas Neue", "Arial Narrow", sans-serif;
    font-size: 170px;
    line-height: 1;
    color: #fff;
    letter-spacing: 2px;
    text-shadow: 6px 6px 0 var(--honey-shadow);
  }
  .claim {
    position: absolute;
    left: 110px; top: 748px;
    width: 576px; height: 64px;
    border: 2px solid var(--cream);
    display: flex; align-items: center; justify-content: center;
    font-size: 32px;
    font-weight: 400;
    color: var(--cream);
    letter-spacing: 1px;
  }
  .origin {
    position: absolute;
    top: 850px; left: 0; width: 800px;
    text-align: center;
    font-family: "Bebas Neue", "Arial Narrow", sans-serif;
    font-size: 240px;
    line-height: 1;
    color: #fff;
    letter-spacing: 8px;
    text-indent: 8px;
    text-shadow: 8px 8px 0 var(--honey-shadow);
  }
</style>
</head>
<body>
<div class="label">
  <div class="ornament ornament--left" role="img" aria-label="Light grey line-drawn wildflowers in the top-left corner"></div>
  <div class="ornament ornament--right" role="img" aria-label="Light grey line-drawn wildflowers in the top-right corner"></div>

  <div class="brand">Sable Creek Market</div>

  <svg class="honey" viewBox="0 0 800 910" preserveAspectRatio="none" aria-hidden="true">
    <defs>
      <linearGradient id="honeyFill" x1="0" y1="0" x2="0" y2="1">
        <stop offset="0" stop-color="#f3a21f"/>
        <stop offset="0.3" stop-color="#f7b326"/>
        <stop offset="0.7" stop-color="#f4801f"/>
        <stop offset="1" stop-color="#ee5b22"/>
      </linearGradient>
    </defs>
    <path d="M0 70 C60 40 110 20 170 32 C230 44 250 78 320 72 C390 66 420 30 480 20 C540 10 570 62 630 60 C690 58 720 20 800 30 L800 910 L0 910 Z" fill="url(#honeyFill)"/>
    <path d="M0 90 C60 62 110 44 170 56 C230 68 250 100 320 94 C390 88 420 54 480 44 C540 34 570 84 630 82 C690 80 720 44 800 54" fill="none" stroke="#f8c63a" stroke-width="10" opacity="0.6"/>
  </svg>

  <div class="bee bee--upper" role="img" aria-label="Small cartoon bee with dotted flight trail"></div>
  <div class="bee bee--lower" role="img" aria-label="Small cartoon bee with dotted flight trail"></div>

  <div class="title-script">Wildflower</div>
  <div class="title-main">HONEY</div>
  <div class="claim">100% PURE &amp; UNFILTERED</div>
  <div class="origin">FLORIDA</div>
</div>
</body>
</html>
```